Small consulting business needs a website designed to highlight value and four offerings

My company is a dynamic consulting firm with four Core Offerings: Learning & Evaluation, Program Management, Facilitation & Coaching; Implementation & Transformation. Our mission is to facilitate organizational change and transformation, and to make space for creativity, joy, belonging, and trust. If done successfully, we grow to better understand ourselves, each other, and the work we do together.

I'd like the website to give a feeling of confidence and clarity. I want the colors to match or compliment my logo. I want to have three tabs - Our Clients, Our Services, and Government.

See attached Word document for additional content. My current website is www.BrightHarborGroup.com.

Some websites I'm inspired by:
https://www.ovalmeadowworks.com
https://www.solvantpartnership.com
https://tqrb.org

Some websites of people/groups in my field that I find uninspiring:
http://danaquillby.com
https://www.moorvale.org

Target Market(s)

State and local government agencies, health tech, and corporate HR departments

Industry/Entity Type

public health, aging, government, health tech

Coding

Number of Pages Required

4 page

Font styles to use
Other font styles liked:
• Calibri and Merriweather

Colors
0054AA
0677BA
7BADD7
CADEEF
E8F1F8
00AB8E
00BBA5
67D7C9
C6EFE9
E9F9F6
FFC000
F8CF3A
FAE287
FDF2CF
FEFAEE
F0912C
F2A743
F7CA91
FBE8D2
FDF5EE

Requirements
Must have
• Attached logo and content, water colors few, and photos.
Nice to have
• Real pictures, which I can provide to the chosen designer
Should not have
• AI generated characters or cartoons.

```html
<!DOCTYPE html>
<html lang="en">
<head>
<meta charset="utf-8">
<title>Bright Harbor Group</title>
<link rel="stylesheet" href="https://fonts.googleapis.com/css2?family=Libre+Baskerville:wght@400;700&family=Jost:wght@400;500;600&display=swap">
<style>
:root{
  --navy:#0b1a5e;
  --blue:#0b4ea2;
  --orange:#f0a43d;
  --orange-soft:#f7ca91;
  --peach:#fdf2e8;
  --sky:#e8f1f8;
  --sky-2:#cadeef;
  --ink:#1b1f3a;
  --muted:#5b5f73;
  --white:#ffffff;
  --serif:"Libre Baskerville", Georgia, serif;
  --sans:"Jost", Arial, sans-serif;
}
*{box-sizing:border-box;margin:0;padding:0}
html,body{width:1200px;height:4493px;overflow:hidden}
body{font-family:var(--sans);color:var(--ink);background:var(--white);position:relative}
.abs{position:absolute}
h1,h2,h3,h4{font-family:var(--serif);font-weight:700;color:var(--navy)}
p{font-size:12.5px;line-height:1.6;color:var(--muted)}

/* Hero */
.hero{left:0;top:0;width:1200px;height:614px;background:linear-gradient(135deg,#0a2fa8 0%,#1d56e6 40%,#6f9fe8 58%,#1a47d4 75%,#0b2fb4 100%)}
.nav{left:0;top:0;width:1200px;height:82px;background:rgba(10,30,110,.35)}
.logo-box{left:150px;top:10px;width:106px;height:60px;background:var(--white);display:flex;align-items:center;gap:6px;padding:6px}
.logo-box .mark{width:18px;height:18px;border-radius:50%;background:var(--orange);flex:none}
.logo-box span{font-family:var(--sans);font-size:9px;line-height:1.2;color:var(--navy)}
.menu{left:460px;top:30px;display:flex;gap:26px;font-size:13px;font-weight:500;color:var(--white)}
.menu .active{color:var(--orange);border-bottom:2px solid var(--orange);padding-bottom:4px}
.cta{left:920px;top:20px;width:128px;height:44px;border:2px solid var(--orange);outline:1px solid var(--orange);outline-offset:3px;color:var(--orange);font-size:13px;font-weight:600;display:flex;align-items:center;justify-content:center}
.hero-panel{left:150px;top:180px;width:555px;height:265px;background:rgba(18,48,150,.78);border-radius:6px;padding:30px}
.hero-panel h1{color:var(--white);font-size:35px;line-height:1.4}
.hero-panel p{color:var(--white);font-size:12.5px;margin-top:12px;max-width:440px}
.arrow-label{top:298px;color:var(--white);font-size:11px;letter-spacing:.5px}

/* Clients */
.clients{left:150px;top:577px;width:900px;height:122px;background:var(--white);box-shadow:0 8px 24px rgba(0,0,0,.1);border-bottom:3px solid var(--orange-soft)}
.clients-tag{left:8px;top:10px;width:176px;height:102px;background:var(--orange);display:flex;align-items:center;padding-left:14px}
.clients-tag h3{color:var(--white);font-size:22px;line-height:1.15}
.client-row{left:220px;top:0;height:122px;width:660px;display:flex;align-items:center;justify-content:space-between}
.client-row span{font-size:15px;font-weight:500;color:#444}

/* Intro */
.center-head{left:0;width:1200px;text-align:center}
.center-head h2{font-size:30px}
.center-sub{left:210px;width:780px;text-align:center}
.vision{left:551px;top:909px;width:499px;height:129px;background:var(--peach);display:flex}
.vision .txt{padding:20px 22px;width:330px}
.vision h4,.mv h4{font-size:15px;margin-bottom:8px}
.mv{left:551px;width:499px}
.dots{left:551px;width:499px;border-top:1.5px dashed #cfd2d8}

/* Offerings */
.num{width:60px;height:60px;border-radius:50%;display:flex;align-items:center;justify-content:center;font-family:var(--serif);font-weight:700;font-size:20px}
.num.solid{background:var(--orange);color:var(--white)}
.num.soft{background:var(--peach);color:var(--orange)}
.offer{width:432px;height:145px;background:var(--peach);padding:18px}
.offer h4{font-size:15px;margin-bottom:10px}
.offer p{font-size:12px;line-height:1.6}
.icon-c{width:117px;height:117px;border-radius:50%;background:var(--blue);display:flex;align-items:center;justify-content:center}
.vline{border-left:2px dashed #e2cfb6}
.hline{border-top:2px solid var(--orange-soft)}

/* Why us */
.why{left:150px;top:2264px;width:900px;height:344px;background:var(--white);box-shadow:0 6px 30px rgba(0,0,0,.08)}
.why h2{font-size:30px}
.feature{width:222px;height:126px;background:var(--sky);padding:14px 12px}
.feature .fhead{display:flex;align-items:center;gap:8px;margin-bottom:10px}
.feature .fhead i{width:34px;height:34px;border-radius:50%;background:var(--orange);flex:none}
.feature h4{font-size:11.5px;line-height:1.3}
.feature p{font-size:12px;line-height:1.5}

/* Help band */
.help{left:0;top:2696px;width:1200px;height:452px;background:linear-gradient(180deg,#13337e 0%,#1c3f86 45%,#0c1f6e 100%)}
.help h2{color:var(--white);font-size:30px}
.pill{width:209px;height:72px;background:var(--white);border-radius:4px;display:flex;align-items:center;justify-content:center;text-align:center;font-size:14.5px;color:var(--navy);padding:0 22px;line-height:1.4}
.btn-out{width:351px;height:52px;border:2px solid var(--white);outline:1px solid var(--white);outline-offset:3px;color:var(--white);font-weight:600;letter-spacing:1.5px;font-size:14px;display:flex;align-items:center;justify-content:center}

/* Collaborate */
.tag{height:30px;background:var(--sky);font-size:12px;font-weight:600;color:var(--navy);display:flex;align-items:center;padding:0 12px}

/* Testimonials */
.quote{width:398px;height:235px;background:var(--peach);padding:26px 28px}
.quote p{font-size:12.5px;line-height:1.55}
.quote h4{font-size:14px;margin-top:18px}
.quote small{font-size:12px;color:var(--muted)}
.qmark{width:56px;height:56px;background:var(--white);display:flex;align-items:center;justify-content:center;font-family:var(--serif);font-size:50px;color:var(--orange-soft);line-height:1;padding-top:18px}
.side-nav{color:#8aa4d6;font-size:12px}

/* Footer */
.footer{left:0;top:4039px;width:1200px;height:454px;background:linear-gradient(160deg,#0d1d6a 0%,#0a1a5c 50%,#081451 100%)}
.input{left:593px;top:4116px;width:457px;height:38px;background:#ffffff33;border:1px solid #ffffff55;color:#d9ddee;font-size:13px;display:flex;align-items:center;padding-left:14px}
.submit{left:593px;top:4168px;width:244px;height:52px;border:2px solid var(--white);outline:1px solid var(--white);outline-offset:3px;color:var(--white);font-weight:600;font-size:14px;letter-spacing:1px;display:flex;align-items:center;justify-content:center}
.foot-logo{left:150px;top:4247px;display:flex;align-items:center;gap:12px}
.foot-logo .mark{width:60px;height:60px;border-radius:50%;background:var(--orange)}
.foot-logo span{font-family:var(--serif);font-size:25px;color:var(--white);line-height:1.35;font-weight:400}
.social{left:846px;top:4285px;display:flex;gap:20px}
.social i{width:24px;height:24px;border-radius:50%;background:var(--white);display:block}
.foot-menu{left:152px;top:4382px;display:flex;gap:26px;color:var(--white);font-size:13px;font-weight:500}
.foot-rule{left:150px;top:4430px;width:910px;border-top:1px solid #ffffff44}
.copy{top:4458px;color:#e6e9f5;font-size:12px}
</style>
</head>
<body>

<!-- Hero -->
<section class="abs hero" role="img" aria-label="Photo of a blue glass atrium ceiling seen from below"></section>
<div class="abs nav"></div>
<div class="abs logo-box"><span class="mark"></span><span>Bright Harbor<br>Group</span></div>
<nav class="abs menu"><span class="active">HOME</span><span>OUR STORY</span><span>SERVICES</span><span>CLIENTS</span><span>GOVERNMENT</span></nav>
<div class="abs cta">CONTACT US</div>
<div class="abs hero-panel">
  <h1>A Seat at the Table for Collaboration, Learning, and Meaningful Change.</h1>
  <p>Bright Harbor Group is a dynamic consulting firm with four Core Offerings: Learning &amp; Evaluation, Program Management, Facilitation &amp; Coaching; Implementation &amp; Transformation</p>
</div>
<div class="abs arrow-label" style="left:22px">&larr;&nbsp; PREV</div>
<div class="abs arrow-label" style="left:1120px">NEXT &nbsp;&rarr;</div>

<!-- Clients -->
<div class="abs clients">
  <div class="abs clients-tag"><h3>Meet Our<br>Clients</h3></div>
  <div class="abs client-row">
    <span>NORVALE</span><span>Oval Meadow</span><span>tandle</span><span>Marrow Institute</span><span>Crestline Health</span><span>Moorvale</span>
  </div>
</div>

<!-- Introducing -->
<div class="abs center-head" style="top:786px"><h2>Introducing us</h2></div>
<p class="abs center-sub" style="top:834px">Bright Harbor Group is a woman-owned business in Oakport, CA, supporting U.S. organizations, communities, and governments through strategic planning, facilitation, and programs that advance health equity and community well-being.</p>

<div class="abs" role="img" aria-label="Watercolor illustration in teal, gold and soft blue" style="left:150px;top:924px;width:331px;height:298px;background:linear-gradient(135deg,#cadeef 0%,#9cc7b7 45%,#f1d58c 100%)"></div>

<div class="abs vision">
  <div class="txt"><h4>Our Vision</h4><p>Our vision is a world where people connect as humans first, growing and evolving together through meaningful collaboration.</p></div>
  <div role="img" aria-label="Watercolor illustration of a sunrise over a path" style="flex:1;background:linear-gradient(160deg,#f6dc93 0%,#bcd8c4 55%,#e8f1f8 100%)"></div>
</div>
<div class="abs mv" style="top:1062px"><h4>Our Mission</h4><p>Our mission is to facilitate organizational change and transformation, and to make space for creativity, joy, belonging, and trust. If done successfully, we grow to better understand ourselves, each other, and the work we do together.</p></div>
<div class="abs dots" style="top:1172px"></div>
<div class="abs mv" style="top:1180px;padding-left:4px"><h4>Our Value</h4><p>We are your steady partner in chaos, driving lasting change through values realignment, expert support, and strategic planning for organizations ready to grow and innovate.</p></div>
<div class="abs dots" style="top:1273px"></div>

<!-- Four Core Offerings -->
<div class="abs center-head" style="top:1358px"><h2>Four Core Offering</h2></div>
<p class="abs center-sub" style="top:1405px">Bright Harbor Group (Bright Harbor) is a values-driven partner with deep roots in multi-sector leadership, adult learning, facilitation, and systems transformation.</p>

<div class="abs vline" style="left:179px;top:1540px;height:102px"></div>
<div class="abs hline" style="left:179px;top:1642px;width:120px"></div>
<div class="abs vline" style="left:511px;top:1650px;height:55px"></div>
<div class="abs vline" style="left:179px;top:1800px;height:46px"></div>
<div class="abs vline" style="left:179px;top:1908px;height:102px"></div>
<div class="abs vline" style="left:511px;top:2010px;height:62px"></div>

<div class="abs num solid" style="left:150px;top:1480px">01</div>
<div class="abs offer" style="left:286px;top:1481px"><h4>Learning &amp; Evaluation</h4><p>Learning and Evaluation is BHG's chief offering. In order for a project to successfully and meaningfully move forward, there are often various administrative, systems, and even interpersonal processes that need to be addressed first....</p></div>
<div class="abs icon-c" style="left:793px;top:1494px"><svg width="56" height="56" viewBox="0 0 56 56" fill="none" stroke="#fff" stroke-width="2"><circle cx="28" cy="20" r="9"/><path d="M24 29v5h8v-5M10 40c8-3 14-3 18 2 4-5 10-5 18-2v8c-8-3-14-3-18 2-4-5-10-5-18-2z"/></svg></div>

<div class="abs icon-c" style="left:290px;top:1677px"><svg width="56" height="56" viewBox="0 0 56 56" fill="none" stroke="#fff" stroke-width="2"><circle cx="28" cy="20" r="8"/><circle cx="28" cy="20" r="3"/><path d="M8 30l8 14h10M48 30l-8 14H30"/></svg></div>
<div class="abs num soft" style="left:481px;top:1705px">02</div>
<div class="abs offer" style="left:617px;top:1664px"><h4>Program Management</h4><p>Multi-Sector Program Management .Whether supporting small community-based programs or managing large-scale efforts, we are skilled at coordinating timelines, resources, and partners to drive projects toward successful outcomes....</p></div>

<div class="abs num soft" style="left:150px;top:1847px">03</div>
<div class="abs offer" style="left:286px;top:1847px"><h4>Facilitation &amp; Coaching</h4><p>Our team has a unique capacity for facilitating honest and open discussions, and encouraging conflict resolution. Very quickly our team can pick up on different perspectives and needs in a room, with this innate skill, guide engagement on complex...</p></div>
<div class="abs icon-c" style="left:793px;top:1860px"><svg width="56" height="56" viewBox="0 0 56 56" fill="none" stroke="#fff" stroke-width="2"><circle cx="42" cy="14" r="4"/><circle cx="14" cy="42" r="4"/><circle cx="24" cy="28" r="5"/><path d="M12 14h22M44 42H22"/></svg></div>

<div class="abs icon-c" style="left:290px;top:2044px"><svg width="56" height="56" viewBox="0 0 56 56" fill="none" stroke="#fff" stroke-width="2"><circle cx="22" cy="26" r="8"/><path d="M19 34v6h6v-6"/><circle cx="40" cy="38" r="6"/><path d="M28 10h16v10"/></svg></div>
<div class="abs num soft" style="left:481px;top:2072px">04</div>
<div class="abs offer" style="left:617px;top:2030px"><h4>Implementation &amp; Transformation</h4><p>BHG's Implementation &amp; Transformation Core Offering is about resource development in action. As resource development experts, BHG helps to build your team's capacity by designing guides and templates....</p></div>

<!-- Why Us -->
<section class="abs why">
  <h2 class="abs" style="left:37px;top:46px">Why Us</h2>
  <p class="abs" style="left:37px;top:100px;width:320px;font-size:12px">Through our Core Offerings and guided by our founder's traditional and nontraditional methods for engaging and steering a team, we create a sense of belonging, foster transparency, and help to build stronger relationships. Our approach helps to drive meaningful change so that organizations and initiatives can clear roadblocks and meet collective goals. Our team's proven ability to transform conflict into opportunity will help to advance your organization and the communities you serve.</p>
  <div class="abs feature" style="left:401px;top:38px"><div class="fhead"><i></i><h4>Strategic &amp; Practical</h4></div><p>We turn vision into action with clear plans and practical support.</p></div>
  <div class="abs feature" style="left:640px;top:38px"><div class="fhead"><i></i><h4>Community-Centered Approach</h4></div><p>We prioritize lived experience, local knowledge, and inclusive collaboration in every project.</p></div>
  <div class="abs feature" style="left:401px;top:179px"><div class="fhead"><i></i><h4>Interdisciplinary Expertise</h4></div><p>Our team blends expertise in public health, strategy, facilitation,planning.</p></div>
  <div class="abs feature" style="left:640px;top:179px"><div class="fhead"><i></i><h4>Collaborative Spirit</h4></div><p>We co-create with partners to foster ownership, alignment, and lasting success.</p></div>
</section>

<!-- We Help Your Team -->
<section class="abs help" role="img" aria-label="Photo of silhouetted people gathered around a glowing globe"></section>
<div class="abs center-head" style="top:2804px"><h2 style="color:#fff">We Help Your Team</h2></div>
<div class="abs pill" style="left:150px;top:2872px">Turn bold visions into practical results.</div>
<div class="abs pill" style="left:380px;top:2872px">Transform conflict into opportunity.</div>
<div class="abs pill" style="left:610px;top:2872px">Strengthen community-led systems.</div>
<div class="abs pill" style="left:841px;top:2872px">Foster a sense of belonging</div>
<div class="abs btn-out" style="left:424px;top:2980px">FIND COMMON GROUND</div>

<!-- We Collaborate With -->
<h2 class="abs" style="left:150px;top:3254px;font-size:30px">We Collaborate With</h2>
<p class="abs" style="left:150px;top:3310px;width:480px">Choose your own adventure with customized proposals and partnerships that help you and your team learn, strategize, and implement together. We can offer an array of services related to project design, management, facilitation, and implementation. Our team can support your learning and quality improvement goal along the way to help align intent with impact. We are a growing, passionate team looking for opportunities to imagine, create, and innovate with you.</p>
<div class="abs" style="left:148px;top:3480px;color:#6b84c4;font-size:14px">&lsaquo;</div>
<div class="abs tag" style="left:168px;top:3472px">Large-scale Companies</div>
<div class="abs tag" style="left:344px;top:3472px">National and local nonprofits</div>
<div class="abs" style="left:548px;top:3480px;color:#6b84c4;font-size:14px">&rsaquo;</div>
<div class="abs" role="img" aria-label="Watercolor illustration in gold and teal tones" style="left:705px;top:3239px;width:345px;height:262px;background:linear-gradient(135deg,#fbe8d2 0%,#f3d27a 40%,#9cc7b7 100%)"></div>

<!-- Testimonials -->
<div class="abs center-head" style="top:3603px"><h2>What Our Customers Say</h2></div>
<p class="abs center-sub" style="top:3650px">From engineers shaping the future to public health experts tackling community challenges, we help a wide range of clients achieve their goals.</p>
<div class="abs side-nav" style="left:110px;top:3828px">&larr; PREV</div>
<div class="abs side-nav" style="left:1032px;top:3828px">NEXT &rarr;</div>
<div class="abs quote" style="left:190px;top:3716px">
  <p>Bright Harbor Group is a phenomenal partner. Maren Holloway is exceptionally knowledgeable about the public health field and brings a collaborative spirit, skillful facilitation, cultural awareness, and meticulous project management to her work. I hope for many more opportunities to work with her.</p>
  <h4>Owen Tallis</h4><small>Moorvale Policy Center</small>
  <div class="abs qmark" style="left:310px;top:170px">&rdquo;</div>
</div>
<div class="abs quote" style="left:612px;top:3716px">
  <p>Bright Harbor Group supported our strategic planning efforts early in our transition from bench research to business operations. Maren is great at helping visualize road maps and therefore planning what is realistic and achievable. We have benefited from the structures came out of engagement with her.</p>
  <h4>Ravi Menon, MSE</h4><small>Tandle Health</small>
  <div class="abs qmark" style="left:310px;top:170px">&rdquo;</div>
</div>

<!-- Footer -->
<footer class="abs footer"></footer>
<p class="abs" style="left:150px;top:4118px;width:380px;color:#e6e9f5">Bright Harbor was created to bring something different to the table: a consulting model that leads with values, honors people's lived experience, and makes space for creativity and joy.</p>
<div class="abs input">Enter Email Address</div>
<div class="abs submit">SUBMIT NOW</div>
<div class="abs foot-logo"><span class="mark"></span><span>Bright Harbor<br>&nbsp;&nbsp;Group</span></div>
<div class="abs social" aria-label="Social links"><i></i><i></i><i></i><i></i><i></i></div>
<nav class="abs foot-menu"><span>HOME</span><span>OUR STORY</span><span>SERVICES</span><span>CLIENTS</span><span>GOVERNMENT</span><span>CONTACT US</span></nav>
<div class="abs foot-rule"></div>
<div class="abs copy" style="left:150px">&copy; Copyright 2025 by Bright Harbor Group</div>
<div class="abs copy" style="left:816px">Terms &amp; Conditions &nbsp;&nbsp;|&nbsp;&nbsp; Privacy Policy</div>

</body>
</html>
```